Design a Bold Tradeshow Backdrop for a Sustainable Cleaning Technology

We need a professional, high-impact 10' × 8' tradeshow backdrop for Vornelle®, a commercial cleaning technology company. 143.75" x 90" high and needs bleeds in the 143.75" direction for printing but the graphic area is 10' wide.

Our first event will have an audience that includes K–12 school administrators, facility managers, business officials, and custodial decision-makers. However, this backdrop will be used at multiple future trade shows across different commercial and institutional markets.

The design therefore needs to be universal rather than specifically education- or school-themed.

Our goal is to stop attendees as they walk past the booth and immediately communicate a simple message:

Safer and more sustainable cleaning can also cost substantially less than conventional cleaning chemicals.

We want the design to feel modern, innovative, clean, sustainable, credible, commercial, and premium. It should resonate with K–12 decision-makers while being equally appropriate at events serving commercial facilities, healthcare, hospitality, government, property management, transportation, and other institutional markets.

It should NOT look like a traditional janitorial supply advertisement and should not be overly busy.

The most important messages need to be understandable from approximately 10–20 feet away.

Required Messaging

The primary headline should be:

SUSTAINABLE CLEANING
DOES NOT HAVE TO BE EXPENSIVE.

Three major value propositions should be prominently displayed:

FREE
Cleaning Chemical Analysis
See how much you can save.

SAVE UP TO 60% or More
on Cleaning Chemical Costs

AS LITTLE AS $0.27/GALLON

We would also like a strong secondary message incorporated into the design:

SMARTER CLEANING.
High Performance. Low Cost. Safer.

Visual Direction — Important

Rather than showing a K–12 school hallway or other environment that limits the backdrop to the education market, we want a sophisticated, universal commercial or institutional environment.

This could be a bright, contemporary commercial facility, lobby, corridor, office environment, public building, or other premium architectural space that could reasonably represent many different types of facilities.

The environment should communicate:

Cleanliness • Safety • Sustainability • Professionalism • Efficiency • High Performance

We want someone from a school, hospital, hotel, office building, airport, government facility, or other commercial property to be able to look at the backdrop and relate the imagery to their own facility.

Please avoid imagery that makes the backdrop industry-specific.

We also want to avoid clichéd environmental imagery. The design does not need to be covered in leaves, trees, water droplets, recycling symbols, or other obvious "green" graphics to communicate sustainability. We prefer a sophisticated commercial interpretation of sustainability.

Color & Brand Direction

We want the overall color palette to stay primarily within:

Blues — consistent with our corporate identity

Greens — to reinforce sustainability, safety, efficiency, and environmental responsibility

White — strongly encouraged for clean space, contrast, and an open contemporary appearance

Black — should be limited primarily to text where necessary for readability

Please avoid making black a major background or dominant design color.

We want the finished display to have a bright, clean, sophisticated, sustainable look and feel rather than a dark or industrial appearance.

The design should use significant negative space and a strong visual hierarchy.

Less is more.

We prefer a few large, powerful messages that can be understood quickly rather than numerous small bullet points, paragraphs, or icons.

Creative Freedom

The attached concept image is provided to communicate our general direction and messaging only.

It does not need to be copied.

We are specifically running this contest because we want designers to improve upon our initial concept and show us different creative approaches to presenting the Vornelle value proposition.

We are open to creative interpretations of the commercial environment, composition, typography, use of negative space, and how the three major financial benefits are presented.

The finished design should feel like an innovative commercial technology brand, not simply another cleaning chemical company.

Corporate Logo — Very Important

We are attaching our official Vornelle® corporate logo for use in the design.

DO NOT redraw, recreate, modify, stylize, reinterpret, trace, or AI-generate the Vornelle logo.

The supplied corporate logo must be inserted directly into the artwork exactly as provided, maintaining its original proportions, colors, typography, trademark elements, and graphic design.

The logo should generally appear in the upper-left area of the backdrop but should not overwhelm the primary marketing message.

Printer Template & Graphic Sizing

We are also attaching the printer's official graphic template and instructions for the 8' × 8' tension-fabric display.

Designers should create their artwork using these supplied specifications so the winning design can be transferred directly into production.

The printer requires that the original document size not be changed, artwork be created on the designated design layer or a new layer, images be embedded, text be converted to outlines, and the finished production artwork be supplied as a PDF.

Please pay particular attention to the bleed area, finished size, and safe artwork area when positioning important text, graphics, and the corporate logo.

Physical Booth Context

The backdrop will sit behind an 8' tradeshow table.

The complete booth will also contain:

A blue stretch tablecloth with the Vornelle corporate logo
BrevoMax and Vornelle product containers and samples on the table
An HulaDrent chemical mixing/dilution station displayed on an elevated stand to the left
A television/monitor to the right demonstrating our online ROI cost-savings calculator

Because these other booth elements will explain our products and technology in greater detail, the backdrop should NOT attempt to explain everything we do.

Its primary purpose is to stop traffic, establish the Vornelle brand, and communicate our core economic and sustainability value proposition.

Final Deliverables

The winning designer must provide artwork properly sized and positioned using our supplied 8' × 8' tension-fabric display template.

Final files should include:

Print-ready, high-resolution PDF
Editable source/vector artwork
All images embedded
Fonts converted to outlines
Artwork correctly positioned within the supplied printer template
Original Vornelle corporate logo incorporated without modification
The 3–5 Second Test

This is perhaps the most important requirement.

Someone walking down a tradeshow aisle should be able to look at the backdrop for 3–5 seconds and understand:

Vornelle offers safer, sustainable, high-performance commercial cleaning — at a lower cost.

The three offers we particularly want them to remember are:

FREE CHEMICAL ANALYSIS

SAVE UP TO 60%

AS LITTLE AS $0.27/GALLON

The overall takeaway should be:

Sustainable cleaning does not have to cost more.

We want the winning design to make that message immediately understandable, credible, and memorable.

Colors
0054AA
0677BA
7BADD7
CADEEF
E8F1F8
0094D4
00A9DD
6FCCEA
C7EBF8
E9F6FB
00AB8E
00BBA5
67D7C9
C6EFE9
E9F9F6
59FF00
82FF00
B8FF75
E3FFCB
F4FFEA

```html
<!DOCTYPE html>
<html lang="en">
<head>
<meta charset="utf-8">
<title>Vornelle – Sustainable Cleaning Backdrop</title>
<link rel="stylesheet" href="https://fonts.googleapis.com/css2?family=Outfit:wght@300;400;500&display=swap">
<style>
  :root {
    --cream: #fbf8f1;
    --navy: #0b2a5b;
    --green: #76a828;
    --gold: #f0b21c;
    --ink: #3f3f3f;
    --ink-soft: #2e2e2e;
    --white: #ffffff;
    --lobby-light: #f3ede2;
    --lobby-mid: #d9cdb8;
    --lobby-glass: #c9d6cf;
  }
  * { margin: 0; padding: 0; box-sizing: border-box; }
  html, body { width: 1200px; height: 1200px; overflow: hidden; background: var(--cream); }
  body { font-family: "Outfit", sans-serif; }

  .backdrop { position: relative; width: 1200px; height: 1200px; background: var(--cream); overflow: hidden; }

  .lobby-photo {
    position: absolute; left: 0; top: 534px; width: 1200px; height: 560px;
    background:
      linear-gradient(180deg, var(--cream) 0%, rgba(251,248,241,0.6) 18%, rgba(251,248,241,0) 45%),
      linear-gradient(90deg, var(--lobby-mid) 0%, var(--lobby-light) 35%, var(--lobby-light) 60%, var(--lobby-glass) 100%);
  }

  .headline { position: absolute; left: 0; width: 1200px; text-align: center; }
  .headline-kicker { top: 88px; font-size: 54px; font-weight: 300; color: var(--ink); letter-spacing: -1px; }
  .headline-main { top: 132px; font-size: 150px; font-weight: 500; color: var(--navy); letter-spacing: -7px; line-height: 1.2; }
  .headline-payoff { top: 338px; font-size: 150px; font-weight: 500; color: var(--green); letter-spacing: -8px; line-height: 1.2; }

  .headline-tag {
    position: absolute; left: 356px; top: 286px; width: 488px; height: 64px;
    background: var(--white); border: 1px solid var(--green);
    transform: rotate(-3deg); box-shadow: 0 6px 14px rgba(0,0,0,0.08);
    display: flex; align-items: center; justify-content: center;
    font-size: 40px; font-weight: 300; color: var(--ink-soft); letter-spacing: -1px;
  }

  .offer { position: absolute; top: 535px; width: 273px; height: 146px; background: var(--white); border-radius: 9px; padding: 16px 0 0 28px; }
  .offer-free { left: 117px; border: 1px solid var(--navy); }
  .offer-save { left: 464px; border: 1px solid var(--gold); }
  .offer-price { left: 810px; border: 1px solid var(--green); }

  .offer-number { position: absolute; top: -30px; left: 26px; font-size: 36px; font-weight: 400; letter-spacing: -2px; line-height: 1; }
  .offer-free .offer-number { color: var(--navy); }
  .offer-save .offer-number { color: var(--gold); }
  .offer-price .offer-number { color: var(--green); }

  .offer-text { font-size: 21px; font-weight: 300; color: var(--ink-soft); line-height: 27px; letter-spacing: -0.3px; }
  .offer-accent { color: var(--green); font-size: 27px; font-weight: 400; }
  .offer-lead { font-size: 19px; font-weight: 400; color: var(--ink-soft); margin-top: 4px; }
  .offer-big { font-size: 35px; font-weight: 400; color: var(--green); line-height: 43px; margin-top: 4px; letter-spacing: -1px; }
  .offer-big .dot { color: var(--ink-soft); }

  .brand-card {
    position: absolute; left: 447px; top: 706px; width: 313px; height: 160px;
    background: var(--white); border: 1px solid var(--navy); border-radius: 8px;
    display: flex; align-items: center; justify-content: center;
  }
  .brand-name { font-size: 50px; font-weight: 500; color: var(--navy); letter-spacing: -1px; }

  .slogan-band {
    position: absolute; left: 0; top: 1093px; width: 1200px; height: 107px;
    background: var(--green); color: var(--white);
    display: flex; align-items: center; justify-content: center;
    font-size: 38px; font-weight: 300; letter-spacing: -1px;
  }
</style>
</head>
<body>
<main class="backdrop">
  <div class="lobby-photo" role="img" aria-label="Bright modern commercial lobby with marble reception desk, wood-slat corridor, lounge chairs and tall glass wall with indoor trees"></div>

  <h1>
    <span class="headline headline-kicker">SUSTAINABLE</span>
    <span class="headline headline-main">CLEANING</span>
    <span class="headline headline-payoff">EXPENSIVE.</span>
    <span class="headline-tag">DOES NOT HAVE TO BE</span>
  </h1>

  <section class="offer offer-free">
    <span class="offer-number">01.</span>
    <p class="offer-text"><span class="offer-accent">FREE</span> Cleaning<br>Chemical Analysis.<br>See how much you<br>can save.</p>
  </section>

  <section class="offer offer-save">
    <span class="offer-number">02.</span>
    <p class="offer-text"><span class="offer-accent">SAVE UP TO 60%</span><br>or More on Cleaning<br>Chemical Costs.</p>
  </section>

  <section class="offer offer-price">
    <span class="offer-number">03.</span>
    <p class="offer-lead">AS LITTLE AS</p>
    <p class="offer-big">$0.27 per<br>GALLON<span class="dot">.</span></p>
  </section>

  <div class="brand-card">
    <span class="brand-name">Vornelle®</span>
  </div>

  <footer class="slogan-band">SMARTER CLEANING. High Performance. Low Cost. Safer."</footer>
</main>
</body>
</html>
```